Endocrinologist needs new stationery

I have a logo from MarkForge and now need stationery with the new logo.

Address: Suite 4, 282 Falcon Street, Richmond, VIC 3121
Phone: 03 9417 2253
Fax: 03 9417 2255
Website: www.drmaylacorwen.com.au
Email: admin@drmaylacorwen.com.au

```html
<!DOCTYPE html>
<html lang="en">
<head>
<meta charset="utf-8">
<title>Dr Mayla Corwen – Stationery</title>
<link rel="stylesheet" href="https://fonts.googleapis.com/css2?family=Open+Sans:wght@400;700&family=Roboto:wght@400;500&display=swap">
<style>
  :root {
    --bg: #e2e2e2;
    --paper: #ffffff;
    --brand-blue: #336e9c;
    --brand-plum: #785469;
    --ink: #555555;
    --ink-soft: #666666;
    --rule: #6f6f6f;
    --card-dark: #1f1f1f;
    --emboss: #3a3a3a;
  }
  * { margin: 0; padding: 0; box-sizing: border-box; }
  html, body { width: 1200px; height: 907px; overflow: hidden; }
  body { background: var(--bg); font-family: "Open Sans", Arial, sans-serif; color: var(--ink); position: relative; }

  .sheet { position: absolute; background: var(--paper); overflow: hidden; }
  .brand-bar { position: absolute; left: 0; bottom: 0; width: 100%; }

  /* Letterhead */
  .letterhead { left: 72px; top: 75px; width: 535px; height: 757px; }
  .letterhead .logo-name { position: absolute; left: 30px; top: 60px; font-size: 19px; color: var(--brand-blue); }
  .letterhead .address { position: absolute; left: 372px; top: 35px; font-size: 8.6px; line-height: 11px; color: var(--ink-soft); }
  .letterhead .contacts { position: absolute; left: 372px; top: 63px; font-size: 8.6px; line-height: 11px; color: var(--ink-soft); list-style: none; }
  .contacts li { display: flex; align-items: center; gap: 3px; }
  .contacts svg { fill: var(--brand-blue); flex: none; }
  .letter { position: absolute; left: 48px; top: 234px; width: 440px; font-family: Roboto, Arial, sans-serif; }
  .letter .salutation { font-size: 12px; font-weight: 500; color: var(--ink); margin-bottom: 18px; }
  .letter p.body { font-size: 9px; line-height: 11px; color: var(--ink-soft); margin-bottom: 10px; }
  .letter .closing { font-size: 7px; font-weight: 500; margin-top: 22px; color: var(--ink); }
  .letter .signature { width: 87px; height: 26px; margin-top: 18px; background: linear-gradient(90deg, #d9d9d9, #eeeeee); border-radius: 3px; }

  /* Business card front */
  .card-front { left: 640px; top: 148px; width: 488px; height: 278px; }
  .card-front .logo-name { position: absolute; right: 24px; top: 48px; font-size: 26px; color: var(--brand-blue); }
  .card-front .holder { position: absolute; left: 23px; top: 135px; width: 442px; border-bottom: 1px solid var(--rule); padding-bottom: 4px; }
  .holder .name { font-size: 18px; font-weight: 700; color: var(--brand-blue); line-height: 22px; }
  .holder .field { font-size: 13.5px; color: var(--ink); line-height: 17px; }
  .card-front .contacts { position: absolute; left: 23px; top: 188px; font-size: 14px; line-height: 17px; color: var(--ink); list-style: none; }
  .card-front .contacts li { gap: 5px; }
  .card-front .address { position: absolute; right: 23px; top: 222px; font-size: 14px; line-height: 17px; text-align: right; color: var(--ink); }

  /* Business card back */
  .card-back { left: 640px; top: 482px; width: 488px; height: 279px; background: var(--card-dark); }
  .card-back .logo-name { position: absolute; left: 0; right: 0; top: 112px; text-align: center; font-size: 34px; color: var(--emboss); }
</style>
</head>
<body>

<!-- Letterhead -->
<section class="sheet letterhead">
  <div class="logo-name">Dr Mayla Corwen</div>

  <address class="address" style="font-style:normal">Suite 4, 282 Falcon Street<br>Richmond, VIC 3121</address>
  <ul class="contacts">
    <li><svg width="8" height="7" viewBox="0 0 10 8"><path d="M1 2c2-2 6-2 8 0v1H7V2H3v1H1zM2 4h6l1 4H1z"/></svg>03 9417 2253</li>
    <li><svg width="8" height="7" viewBox="0 0 10 8"><path d="M3 0h4v2H3zM1 3h8v5H1zm2 2v1h4V5z"/></svg>03 9417 2255</li>
    <li><svg width="8" height="7" viewBox="0 0 10 8"><path d="M0 3l5-3 5 3v5H0zm1 0l4 3 4-3-4-2z"/></svg>admin@drmaylacorwen.com.au</li>
    <li><svg width="8" height="8" viewBox="0 0 10 10"><circle cx="5" cy="5" r="5"/></svg>www.drmaylacorwen.com.au</li>
  </ul>

  <div class="letter">
    <p class="salutation">Dear Mr. Hollis,</p>
    <p class="body">Lorem ipsum dolor sit amet, consectetuer adipiscing elit, sed diam nonmmy nibh euismod tincidunt ut laor eet dolore magna aliquam erat volutpat. Ut wisi enim ad minim veniam, quis nostrud exerci tationmcorper suscipit lobortis nisl ut aliquip ex ea commodo consequat. Duis autem vel eum iriure dolor in hendrerit in vulputate velit esse molestie consequat, vel illum dolore eu feugiat</p>
    <p class="body">Rorem ipsum dolor sit amet, consectetuer adipiscing elit, sed diam nonmmy nibh euismod tincidunt ut laor eet dolore magna aliquam erat volutpat. Ut wisi enim ad minim veniam, quis nostrud exerci tationmcorper suscipit lobortis nisl ut aliquip ex ea commodo consequat. Duis autem vel eum iriure dolor in hendrerit in vulputate velit esse molest</p>
    <p class="body">Dorem ipsum dolor sit amet, consectetuer adipiscing elit, sed diam nonmmy nibh euismod tincidunt ut laor eet dolore magna aliquam erat volutpat. Ut wisi enim ad minim veniam, quis nostrud exerci tationmcorper suscipit lobortis nisl ut aliquip ex ea commodo consequat. Duis autem vel eum iriure dolor in hendrerit in suscipit lobortis nisl ut aliquip ex ea commodo consequat. Duis autem vel eum iriure dolor in hendrerit in vulputate velit esse molestie consequat, vel illum</p>
    <p class="body">Sorem ipsum dolor sit amet, consectetuer adipiscing elit, sed diam nonmmy nibh euismod tincidunt ut laor eet dolore magna aliquam erat volutpat. Ut wisi enim ad minim veniam, quis nostrud exerci tationmcorper suscipit lobortis nisl ut aliquip ex ea commodo consequat. Duis autem vel eum iriure dolor in</p>
    <p class="closing">Sincerely,</p>
    <div class="signature" role="img" aria-label="Handwritten signature"></div>
  </div>

  <svg class="brand-bar" width="535" height="13" viewBox="0 0 535 13">
    <polygon points="0,0 372,0 360,13 0,13" fill="var(--brand-blue)"/>
    <polygon points="382,0 535,0 535,13 370,13" fill="var(--brand-plum)"/>
  </svg>
</section>

<!-- Business card front -->
<section class="sheet card-front">
  <div class="logo-name">Dr Mayla Corwen</div>

  <div class="holder">
    <div class="name">DR MAYLA CORWEN</div>
    <div class="field">ENDOCRINOLOGY</div>
  </div>

  <ul class="contacts">
    <li><svg width="12" height="10" viewBox="0 0 10 8"><path d="M1 2c2-2 6-2 8 0v1H7V2H3v1H1zM2 4h6l1 4H1z"/></svg>03 9417 2253</li>
    <li><svg width="12" height="10" viewBox="0 0 10 8"><path d="M3 0h4v2H3zM1 3h8v5H1zm2 2v1h4V5z"/></svg>03 9417 2255</li>
    <li><svg width="12" height="10" viewBox="0 0 10 8"><path d="M0 3l5-3 5 3v5H0zm1 0l4 3 4-3-4-2z"/></svg>admin@drmaylacorwen.com.au</li>
    <li><svg width="12" height="12" viewBox="0 0 10 10"><circle cx="5" cy="5" r="5"/></svg>www.drmaylacorwen.com.au</li>
  </ul>

  <address class="address" style="font-style:normal">Suite 4, 282 Falcon Street<br>Richmond, VIC 3121</address>

  <svg class="brand-bar" width="488" height="11" viewBox="0 0 488 11">
    <polygon points="0,0 341,0 332,11 0,11" fill="var(--brand-blue)"/>
    <polygon points="350,0 488,0 488,11 341,11" fill="var(--brand-plum)"/>
  </svg>
</section>

<!-- Business card back -->
<section class="sheet card-back">
  <div class="logo-name">Dr Mayla Corwen</div>
</section>

</body>
</html>
```